Corvane Collective Web Presence Design and Relaunch

Take existing web files and "clean up" for a a more presentable web landing pad.
posted presently on a site pad CSS template. at www.corvanecollective.org

The site is clunky and unprofessional looking. Needs to be toned down so the urgency is conveyed, but not via a burning planet image.

Target Market(s)

Non-profit climate adaptation group targeting local government land management agencies, special districts and private landholders of natural resource properties.

Industry/Entity Type

Environment

Coding

Coded - Design and coding required

Number of Pages Required

4 page

Font styles to use
Serif
Sans Serif

Requirements
Must have
• Include current logos, aspects if content on current site www.corvanecollective.org
• A regional Pacific Northwest Focus (US & Canada). Content speaking to urgency but respectful of cultural diversity and norms. Sustainability themes. Emphasis on action and implementation.
Nice to have
• link to like minded projects. Appear to future generations. Diversity in thematic areas ecological resiliency, energy, food security and infrastructure.

```html
<!DOCTYPE html>
<html lang="en">
<head>
<meta charset="utf-8">
<title>Corvane Collective – Implementing Climate Strategies</title>
<link rel="stylesheet" href="https://fonts.googleapis.com/css2?family=Poppins:wght@300;400;500;600;700&family=Merriweather:wght@700&display=swap">
<style>
:root{
  --green:#8cc63f;
  --green-dark:#6aa520;
  --green-pale:#eef6e2;
  --blue:#0f8ccf;
  --blue-dark:#0a6fa6;
  --ink:#2f2f2f;
  --muted:#777;
  --line:#e3e3e3;
  --white:#fff;
}
*{box-sizing:border-box;margin:0;padding:0}
html,body{width:1200px;height:4456px;overflow:hidden}
body{position:relative;background:var(--white);font-family:"Poppins",Arial,sans-serif;color:var(--ink)}
.abs{position:absolute}
.photo{position:absolute}
/* header */
.brand{left:80px;top:30px;display:flex;align-items:center;gap:12px;z-index:3}
.brand-mark{width:22px;height:22px;border-radius:50%;background:var(--green)}
.brand-name{font-size:26px;font-weight:600;color:var(--white);line-height:1.1;width:160px}
.nav{left:530px;top:42px;display:flex;gap:26px;font-size:14px;font-weight:500;color:var(--white);z-index:3}
.nav .active{color:var(--blue);border-bottom:2px solid var(--blue)}
.call{left:912px;top:0;width:288px;height:98px;background:var(--green);border-bottom-left-radius:50px;z-index:3;display:flex;align-items:center;padding-left:22px;gap:16px;color:var(--white)}
.call-icon{width:56px;height:56px;border-radius:50%;background:var(--white);display:flex;align-items:center;justify-content:center}
.call small{display:block;font-size:13px}
.call strong{font-size:26px;font-weight:600}
/* hero */
.hero{left:0;top:0;width:1200px;height:760px;background:radial-gradient(circle at 62% 38%,#b9d98a 0,#7fa84d 22%,#a9c9a0 45%,#d5e6ee 80%)}
.hero-eyebrow{left:80px;top:206px;font-size:26px;font-weight:500;color:var(--white)}
.hero-title{left:80px;top:248px;font-family:"Merriweather",Georgia,serif;font-size:52px;line-height:1.22;color:#1c1c1c;width:500px}
.btn{display:inline-flex;align-items:center;gap:14px;height:56px;padding:0 6px 0 28px;border-radius:28px;font-size:15px;font-weight:600;color:var(--white);text-transform:uppercase}
.btn-blue{background:var(--blue)}
.btn-green{background:var(--green)}
.btn i{width:46px;height:46px;border-radius:50%;background:var(--white);display:block}
.hero-btn{left:80px;top:436px}
.hero-arrows{left:972px;top:566px;display:flex;gap:8px}
.hero-arrows span{width:46px;height:46px;border-radius:50%;background:var(--blue);display:block}
.hero-arrows span+span{background:var(--white)}
.hero-wave{left:0;top:560px;width:1200px;height:260px}
/* section titles */
.sec-title{position:absolute;left:0;width:1200px;text-align:center;font-size:38px;font-weight:600;text-transform:uppercase;color:var(--ink)}
.sec-title em{font-style:normal;color:var(--green)}
.sec-sub{position:absolute;left:0;width:1200px;text-align:center;font-size:14px;color:var(--green)}
/* featured */
.feat-band{left:0;top:1080px;width:1200px;height:220px;background:var(--green-pale)}
.card{position:absolute;top:1000px;height:352px;background:var(--white);border:1px solid var(--line);text-align:center;padding:44px 26px 0}
.card-icon{width:64px;height:64px;margin:0 auto 24px;border:3px solid var(--blue);border-radius:10px}
.card h3{font-size:21px;font-weight:600;line-height:1.3;margin-bottom:14px}
.card p{font-size:14px;line-height:1.7;color:var(--muted)}
.card-active{top:960px;height:440px;background:var(--green);border-color:var(--green);color:var(--white)}
.card-active .card-icon{border-color:var(--white);border-radius:50%}
.card-active p{color:var(--white)}
.card-arrow{left:444px;top:1356px;width:52px;height:52px;border-radius:50%;background:var(--blue-dark)}
/* stats */
.stat{position:absolute;top:1580px;width:240px;text-align:center}
.stat-icon{width:56px;height:56px;margin:0 auto 20px;border-radius:50%;background:var(--blue);opacity:.85}
.stat b{display:block;font-size:40px;font-weight:700}
.stat span{font-size:16px;color:var(--muted)}
.stat-btns{left:0;top:1766px;width:1200px;display:flex;justify-content:center;gap:14px}
/* about */
.about-photo{left:0;top:1960px;width:1200px;height:640px;background:linear-gradient(180deg,#bfd7ea 0,#e7eef2 35%,#4c5a6a 55%,#6c8a3c 80%,#8aa84e 100%)}
.about-box{left:188px;top:1912px;width:372px;height:450px;background:var(--white);padding:40px 40px;box-shadow:0 6px 20px rgba(0,0,0,.12)}
.about-box h2{font-size:38px;font-weight:600;text-transform:uppercase;color:var(--green)}
.about-box h2 em{font-style:normal;color:var(--ink)}
.about-box .sub{font-size:13px;color:var(--green);margin:4px 0 18px}
.about-box p{font-size:14px;line-height:1.7;color:var(--muted);margin-bottom:24px}
.about-wave{left:0;top:2420px;width:1200px;height:260px}
/* think green */
.globe{left:395px;top:2836px;width:420px;height:420px;border-radius:50%;background:radial-gradient(circle at 40% 40%,#6fb3d8 0,#3d87b5 35%,#4f8a2c 60%,#2d5a18 100%)}
.metric{position:absolute;width:220px}
.metric b{display:block;font-size:40px;font-weight:500;color:var(--blue);line-height:1.2}
.metric span{font-size:18px;font-weight:600}
.metric.left{text-align:right}
.dot{position:absolute;width:20px;height:20px;border-radius:50%;background:var(--line);border:4px solid #f4f4f4}
/* recent work */
.work{position:absolute;top:3384px;width:248px;text-align:center}
.work .photo{position:relative;height:264px}
.work h4{font-size:17px;font-weight:600;margin-top:28px}
.work p{font-size:13px;color:var(--muted);margin-top:4px}
/* newsletter */
.news-wave{left:0;top:3950px;width:1200px;height:260px}
.news{left:240px;top:3860px;width:720px;height:300px;background:var(--green);text-align:center;color:var(--white);padding-top:44px}
.news h2{font-size:38px;font-weight:600;text-transform:uppercase}
.news p{font-size:14px;margin-top:6px}
.news-form{margin:28px auto 0;width:600px;height:58px;background:var(--white);border-radius:29px;display:flex;align-items:center;justify-content:space-between;padding:0 6px 0 28px;color:#aaa;font-size:14px}
/* footer */
.foot-brand{left:140px;top:4210px;display:flex;align-items:center;gap:12px}
.foot-brand .brand-name{color:var(--green);font-size:24px}
.foot-col{position:absolute;top:4228px;font-size:14px;color:var(--muted)}
.foot-col h5{font-size:16px;font-weight:600;color:var(--ink);text-transform:uppercase;margin-bottom:14px}
.foot-col li{list-style:none;line-height:1.8}
.foot-col li::before{content:"›";color:var(--green);margin-right:8px}
.contact-row{display:flex;gap:10px;align-items:flex-start;line-height:1.5;margin-bottom:10px}
.contact-row i{width:14px;height:14px;border-radius:50%;background:var(--green);flex:none;margin-top:4px}
.socials{display:flex;gap:8px}
.socials span{width:32px;height:32px;border-radius:50%;background:var(--blue);display:block}
.socials span:nth-child(2n){background:var(--green)}
.copy{left:0;top:4412px;width:1200px;text-align:center;font-size:13px;color:var(--muted)}
.copy b{color:var(--green);font-weight:500}
</style>
</head>
<body>

<!-- hero -->
<div class="photo hero" role="img" aria-label="Hand holding a small tree with soil against a soft green background"></div>
<svg class="abs hero-wave" viewBox="0 0 1200 260" preserveAspectRatio="none" aria-hidden="true">
  <path d="M0 150 C300 260 700 40 1200 120 L1200 260 L0 260Z" fill="#fff"/>
  <path d="M0 140 C300 250 700 30 1200 110" fill="none" stroke="#8cc63f" stroke-width="2"/>
  <path d="M0 160 C320 240 720 60 1200 140" fill="none" stroke="#8cc63f" stroke-width="1.5" opacity=".6"/>
  <path d="M0 180 C340 250 740 80 1200 160" fill="none" stroke="#8cc63f" stroke-width="1" opacity=".4"/>
</svg>

<div class="abs brand"><span class="brand-mark"></span><span class="brand-name">Corvane Collective</span></div>
<nav class="abs nav"><span class="active">HOME</span><span>ABOUT</span><span>OUR PROJECTS</span><span>EVENTS</span></nav>
<div class="abs call">
  <span class="call-icon"><svg width="26" height="26" viewBox="0 0 24 24"><path d="M6.6 10.8a15 15 0 006.6 6.6l2.2-2.2a1 1 0 011-.25 11.4 11.4 0 003.6.57 1 1 0 011 1V20a1 1 0 01-1 1A17 17 0 013 4a1 1 0 011-1h3.5a1 1 0 011 1c0 1.25.2 2.45.57 3.57a1 1 0 01-.25 1z" fill="#0f8ccf"/></svg></span>
  <div><small>Call us now</small><strong>555 014 2290</strong></div>
</div>

<div class="abs hero-eyebrow">Climate Adaptation</div>
<h1 class="abs hero-title">Implementing Climate Strategies</h1>
<div class="abs hero-btn btn btn-blue">Contact us <i></i></div>
<div class="abs hero-arrows"><span></span><span></span></div>

<!-- featured project -->
<h2 class="sec-title" style="top:832px"><em>Featured</em> Project</h2>
<div class="sec-sub" style="top:896px">Corvane Collective</div>
<div class="abs feat-band"></div>
<div class="card" style="left:88px;width:240px"><div class="card-icon"></div><h3>Adaptation Plans</h3><p>Communities throughout the region have adopted plans to address our changing climate.</p></div>
<div class="card card-active" style="left:340px;width:260px"><div class="card-icon"></div><h3>On The ground...</h3><p>The collective is nimble and growing throughout the region. Presently we lend our support to grassroots watersheds in the Cascadia.</p></div>
<div class="card" style="left:620px;width:240px"><div class="card-icon"></div><h3>Ecological Resilience</h3><p>To endure change, communities need to keep their watersheds from failing. Our network.</p></div>
<div class="card" style="left:872px;width:248px"><div class="card-icon"></div><h3>Energy and Food</h3><p>Security of community food and energy flows, and always will be, an essential component of food.</p></div>
<div class="abs card-arrow"></div>

<!-- what we are doing -->
<h2 class="sec-title" style="top:1474px"><em>What we</em> are doing ?</h2>
<div class="stat" style="left:88px"><div class="stat-icon"></div><b>250+</b><span>Project Completed</span></div>
<div class="stat" style="left:352px"><div class="stat-icon"></div><b>300+</b><span>Donations</span></div>
<div class="stat" style="left:612px"><div class="stat-icon"></div><b>17+</b><span>Communities Engaged</span></div>
<div class="stat" style="left:880px"><div class="stat-icon"></div><b>70+</b><span>Volunteers</span></div>
<div class="abs stat-btns"><span class="btn btn-blue">Join us today <i></i></span><span class="btn btn-green">Contact now <i></i></span></div>

<!-- about -->
<div class="photo about-photo" role="img" aria-label="Solar panel array on a green hillside under a bright sky"></div>
<svg class="abs about-wave" viewBox="0 0 1200 260" preserveAspectRatio="none" aria-hidden="true">
  <path d="M0 120 C400 40 800 260 1200 140 L1200 260 L0 260Z" fill="#fff"/>
  <path d="M0 110 C400 30 800 250 1200 130" fill="none" stroke="#8cc63f" stroke-width="2"/>
  <path d="M0 130 C420 50 820 240 1200 150" fill="none" stroke="#8cc63f" stroke-width="1.5" opacity=".6"/>
</svg>
<div class="abs about-box">
  <h2>About <em>us</em></h2>
  <div class="sub">Corvane Collective</div>
  <p>Founded in 2019, the Corvane Collective draws from decades of commitment and action. A core group of committed professionals and community leaders have come together to grow and build a network of people who want to secure our next generation future.</p>
  <span class="btn btn-blue">Learn more <i></i></span>
</div>

<!-- think green -->
<h2 class="sec-title" style="top:2722px"><em>Think Green !</em> Save Money</h2>
<div class="photo globe" role="img" aria-label="Earth globe wrapped in green grass recycling arrows"></div>
<div class="metric left" style="left:120px;top:2880px"><b>98%</b><span>Clean Water</span></div>
<div class="metric left" style="left:120px;top:3072px"><b>56%</b><span>Forest Rescue</span></div>
<div class="metric" style="left:852px;top:2880px"><b>77%</b><span>Agriculture</span></div>
<div class="metric" style="left:852px;top:3072px"><b>84%</b><span>Alternative energy</span></div>
<span class="dot" style="left:370px;top:2920px"></span>
<span class="dot" style="left:370px;top:3112px"></span>
<span class="dot" style="left:822px;top:2920px"></span>
<span class="dot" style="left:822px;top:3112px"></span>

<!-- recent work -->
<h2 class="sec-title" style="top:3306px"><em>Recent</em> Work</h2>
<div class="work" style="left:80px"><div class="photo" role="img" aria-label="Wind turbines and solar panels on a green field" style="background:linear-gradient(180deg,#b7d3ea,#6f98b8 55%,#4d6b3a)"></div><h4>Energy</h4><p>Investment in clean energy</p></div>
<div class="work" style="left:344px"><div class="photo" role="img" aria-label="Hands holding freshly harvested green grain" style="background:linear-gradient(180deg,#6da23a,#3f7a1e)"></div><h4>Food Security</h4><p>Investment in clean energy</p></div>
<div class="work" style="left:608px"><div class="photo" role="img" aria-label="River winding through a forested valley" style="background:linear-gradient(180deg,#c9a27a,#7c6a4c 50%,#3b5a3a)"></div><h4>Ecological Resilience</h4><p>Environmental Progress</p></div>
<div class="work" style="left:872px"><div class="photo" role="img" aria-label="Aerial view of a coastal city and bridges" style="background:linear-gradient(180deg,#8ab0cf,#4f6f8c 55%,#6a7a86)"></div><h4>Infrastructure</h4><p>Lorem ipsum</p></div>

<!-- newsletter -->
<svg class="abs news-wave" viewBox="0 0 1200 260" preserveAspectRatio="none" aria-hidden="true">
  <path d="M0 60 C400 200 800 -20 1200 90" fill="none" stroke="#8cc63f" stroke-width="2"/>
  <path d="M0 80 C420 210 820 0 1200 110" fill="none" stroke="#8cc63f" stroke-width="1.5" opacity=".6"/>
  <path d="M0 100 C440 220 840 20 1200 130" fill="none" stroke="#8cc63f" stroke-width="1" opacity=".4"/>
</svg>
<div class="abs news">
  <h2>Sign up for newsletter !</h2>
  <p>Would you like to receive our seasonal updates? Sign up</p>
  <div class="news-form"><span>Enter Email *</span><span class="btn btn-blue" style="height:48px">Subscribe <i style="width:38px;height:38px"></i></span></div>
</div>

<!-- footer -->
<div class="abs foot-brand"><span class="brand-mark"></span><span class="brand-name">Corvane Collective</span></div>
<div class="foot-col" style="left:348px"><h5>Sitemap</h5><ul><li>About Us</li><li>Causes</li><li>Testimonial</li><li>Events</li><li>Contact Us</li></ul></div>
<div class="foot-col" style="left:612px;width:220px"><h5>Contact us</h5>
  <div class="contact-row"><i></i><span>418 Alderwood Lane, Bellgrove WA 98201</span></div>
  <div class="contact-row"><i></i><span>555-021-4478</span></div>
  <div class="contact-row"><i></i><span>info@corvanecollective.org</span></div>
</div>
<div class="foot-col" style="left:872px"><h5>Follow us</h5><div class="socials"><span></span><span></span><span></span><span></span><span></span></div></div>
<div class="abs copy">© <b>Corvane Collective</b> • 2020 All rights reserved.</div>

</body>
</html>
```